Business Card Design for Online Gift Business

Business card design for a new online Canadian company called "Harlow & Reed Gift Crates" selling modern and luxurious gift boxes for every occasion. Items are sourced locally from talented socially-responsible Canadian artisans. Each gift is elegantly presented in a keepsake wood box to ensure a lasting impression.

Industry/Entity Type

E-Commerce

Contact Information for Business Card

Merin Holloway, Proprietor
Calgary, AB
587-214-3306
www.harlowandreed.ca
hello@harlowandreed.ca

Requirements
Must have
• Gifts from our best, to your best
• Please also include the symbols for Facebook and Instagram
Nice to have
• **I have attached a few samples of background colors and font colors that I like. I hope this helps in a few directions to try.

```html
<!DOCTYPE html>
<html lang="en">
<head>
<meta charset="utf-8">
<title>Harlow &amp; Reed Gift Crates — Business Card</title>
<link rel="stylesheet" href="https://fonts.googleapis.com/css2?family=Montserrat:wght@700&family=Quicksand:wght@500;600&display=swap">
<style>
  :root {
    --page: #f3f2f0;
    --bark-dark: #2a140e;
    --bark: #3e2219;
    --tan: #a88b68;
    --tan-deep: #8c6e4c;
    --gold: #c7a06a;
    --cream: #e6d8c3;
    --cream-deep: #d9c6aa;
    --logo-ink: #8a6a4a;
    --white: #ffffff;
  }
  * { box-sizing: border-box; margin: 0; padding: 0; }
  html, body { width: 1200px; height: 800px; overflow: hidden; }
  body {
    background: var(--page);
    font-family: "Quicksand", sans-serif;
    position: relative;
  }
  .card {
    position: absolute;
    top: 250px;
    width: 520px;
    height: 300px;
    border-radius: 3px;
    overflow: hidden;
    box-shadow: 0 6px 18px rgba(40, 20, 10, 0.22);
  }
  .card--front { left: 50px; }
  .card--back { left: 630px; }

  .pattern-field {
    position: absolute;
    inset: 0;
    background:
      radial-gradient(circle at 30% 40%, rgba(199,160,106,0.35), transparent 60%),
      linear-gradient(135deg, var(--tan) 0%, var(--tan-deep) 100%);
  }

  .band {
    position: absolute;
    left: 0; right: 0;
    background: linear-gradient(90deg, var(--bark-dark), var(--bark));
  }

  /* Front */
  .card--front .band--top { top: 0; height: 24px; }
  .card--front .band--bottom {
    bottom: 0; height: 30px;
    display: flex; align-items: center; justify-content: center;
  }
  .tagline {
    color: var(--cream);
    font-size: 12px;
    font-weight: 500;
    letter-spacing: 1.5px;
  }
  .logo-panel {
    position: absolute;
    left: 70px; top: 72px;
    width: 380px; height: 132px;
    border-radius: 16px;
    background: linear-gradient(180deg, var(--cream), var(--cream-deep));
    display: flex;
    align-items: center;
    justify-content: center;
    padding: 0 20px;
  }
  .brand-name {
    font-family: "Quicksand", sans-serif;
    font-weight: 600;
    color: var(--logo-ink);
    white-space: nowrap;
  }
  .logo-panel .brand-name { font-size: 24px; }

  /* Back */
  .card--back .band--bottom { bottom: 0; height: 108px; }
  .logo-panel--small {
    left: 24px; top: 22px;
    width: 230px; height: 70px;
    border-radius: 10px;
    padding: 0 12px;
  }
  .logo-panel--small .brand-name { font-size: 14px; }
  .name-plate {
    position: absolute;
    right: 22px; top: 118px;
    width: 236px; height: 62px;
    border-radius: 10px;
    background: linear-gradient(90deg, var(--bark-dark), var(--bark));
    padding: 11px 16px;
    color: var(--white);
    z-index: 1;
  }
  .name-plate__name {
    font-family: "Montserrat", sans-serif;
    font-weight: 700;
    font-size: 16px;
    letter-spacing: 0.5px;
    text-transform: uppercase;
  }
  .name-plate__role {
    font-size: 13px;
    font-weight: 500;
    margin-top: 2px;
  }
  .contact-list {
    position: absolute;
    left: 20px; right: 20px;
    list-style: none;
    display: flex;
    align-items: center;
    justify-content: space-between;
    color: var(--white);
    font-size: 12px;
    font-weight: 500;
  }
  .contact-list--primary { bottom: 50px; }
  .contact-list--secondary { bottom: 14px; }
  .contact-item { display: flex; align-items: center; gap: 8px; }
  .contact-icon {
    width: 24px; height: 24px;
    border-radius: 50%;
    background: var(--white);
    display: flex; align-items: center; justify-content: center;
    flex: none;
  }
  .contact-icon svg { width: 14px; height: 14px; fill: var(--bark); }
  .social-set { display: flex; align-items: center; gap: 8px; }
  .social-dot {
    width: 24px; height: 24px;
    border-radius: 50%;
    background: var(--white);
    flex: none;
  }
</style>
</head>
<body>

<section class="card card--front" aria-label="Business card front">
  <div class="pattern-field" role="img" aria-label="Tan and gold interlocking circle pattern"></div>
  <div class="band band--top"></div>
  <div class="logo-panel">
    <span class="brand-name">Harlow &amp; Reed Gift Crates</span>
  </div>
  <div class="band band--bottom">
    <p class="tagline">Gifts from our best, to your best</p>
  </div>
</section>

<section class="card card--back" aria-label="Business card back">
  <div class="pattern-field" role="img" aria-label="Tan and gold interlocking circle pattern"></div>
  <div class="logo-panel logo-panel--small">
    <span class="brand-name">Harlow &amp; Reed Gift Crates</span>
  </div>
  <div class="band band--bottom"></div>
  <div class="name-plate">
    <p class="name-plate__name">Merin Holloway</p>
    <p class="name-plate__role">Proprietor</p>
  </div>
  <ul class="contact-list contact-list--primary">
    <li class="contact-item">
      <span class="contact-icon">
        <svg viewBox="0 0 24 24" aria-hidden="true"><path d="M6.6 10.8a15.1 15.1 0 0 0 6.6 6.6l2.2-2.2a1 1 0 0 1 1-.25 11.4 11.4 0 0 0 3.6.57 1 1 0 0 1 1 1V20a1 1 0 0 1-1 1A17 17 0 0 1 3 4a1 1 0 0 1 1-1h3.5a1 1 0 0 1 1 1c0 1.25.2 2.45.57 3.6a1 1 0 0 1-.25 1z"/></svg>
      </span>
      <span>587-214-3306</span>
    </li>
    <li class="contact-item">
      <span class="contact-icon">
        <svg viewBox="0 0 24 24" aria-hidden="true"><path d="M3 4h18a1 1 0 0 1 1 1v11a1 1 0 0 1-1 1h-7v2h3v2H7v-2h3v-2H3a1 1 0 0 1-1-1V5a1 1 0 0 1 1-1zm1 2v9h16V6z"/></svg>
      </span>
      <span>www.harlowandreed.ca</span>
    </li>
    <li class="contact-item">
      <span class="contact-icon">
        <svg viewBox="0 0 24 24" aria-hidden="true"><path d="M12 2a7 7 0 0 0-7 7c0 5.25 7 13 7 13s7-7.75 7-13a7 7 0 0 0-7-7zm0 9.5A2.5 2.5 0 1 1 12 6.5a2.5 2.5 0 0 1 0 5z"/></svg>
      </span>
      <span>Calgary, AB</span>
    </li>
  </ul>
  <ul class="contact-list contact-list--secondary">
    <li class="contact-item">
      <span class="contact-icon">
        <svg viewBox="0 0 24 24" aria-hidden="true"><path d="M3 5h18a1 1 0 0 1 1 1v12a1 1 0 0 1-1 1H3a1 1 0 0 1-1-1V6a1 1 0 0 1 1-1zm1 2.4V17h16V7.4l-8 5.2z M4.6 7 12 11.8 19.4 7z"/></svg>
      </span>
      <span>hello@harlowandreed.ca</span>
    </li>
    <li class="contact-item">
      <span class="social-set" aria-label="Social media profiles">
        <span class="social-dot" aria-hidden="true"></span>
        <span class="social-dot" aria-hidden="true"></span>
      </span>
      <span>@harlowandreed</span>
    </li>
  </ul>
</section>

</body>
</html>
```